New Generation Winery needs inspiring label for special bottling

We are a family owned winery in the Rhine Valley in Germany. Check www.brandl-kohlmann.de . We have a very exciting project going: In 2014 we harvested our best vinyard and split the grapes in half. First half I have treated the way I have done it over the past 40 years. Second half I gave to my daughter who is just entering the winemaking business. She has treated it in a completely different way - her way - the way of the new generation. One of the differentiators; she has squeezed the juices with her bare feet which reduces acidity and bitterness in the wine (less tannins). This is why we want to call the wine "Kieselwind" (meaning "Pebblewind"). Please be careful when writing the "ß" . It is a German letter which replaces the "double s". It is NOT a capital B!! I Have attached a file which gives you the size of the label and another file which shows the current design of the winery labels. If possible it should pick up some elements from the current design (maybe just the colours?) but otherwise you are free. It will go on a dark green bottle, almost black. Apart from the word "Kieselwind" you need to place the grape "Riesling", the word "trocken" (means dry) and the year of the harvest "2014".

Industry/Entity Type

Brandl

Requirements
Nice to have
• Update 25.3.2015: Have a look at the attached image "Inspiration". Maybe that is a good thought starter, too. Have fun..

```html
<!DOCTYPE html>
<html lang="de">
<head>
<meta charset="utf-8">
<title>Kieselwind Riesling – Etikett</title>
<link rel="stylesheet" href="https://fonts.googleapis.com/css2?family=Cormorant+Garamond:ital,wght@1,500&family=Archivo+Black&family=Arimo:wght@400&display=swap">
<style>
  :root {
    --stage: #5e5e5e;
    --label-paper: #f2efd1;
    --ink: #555555;
    --ink-dark: #1a1a1a;
    --splash-red: #d6365f;
    --splash-violet: #8e5fa8;
    --splash-blue: #2f7fbf;
    --rim-1: #3aa655;
    --rim-2: #e8c22a;
    --rim-3: #d8432f;
    --rim-4: #8c3fa6;
    --rim-5: #2c6fc4;
  }
  * { box-sizing: border-box; margin: 0; padding: 0; }
  html, body {
    width: 779px;
    height: 1200px;
    overflow: hidden;
    background: var(--stage);
  }
  .stage {
    position: relative;
    width: 779px;
    height: 1200px;
  }
  .wine-label {
    position: absolute;
    left: 110px;
    top: 280px;
    width: 560px;
    height: 640px;
    padding: 4px;
    background: linear-gradient(135deg, var(--rim-1), var(--rim-2), var(--rim-3), var(--rim-4), var(--rim-5), var(--rim-1));
  }
  .wine-label__paper {
    position: relative;
    width: 100%;
    height: 100%;
    background: var(--label-paper);
  }
  .wine-label__name {
    position: absolute;
    top: 86px;
    left: 0;
    width: 100%;
    text-align: center;
    font-family: "Cormorant Garamond", Georgia, serif;
    font-style: italic;
    font-weight: 500;
    font-size: 56px;
    line-height: 1;
    color: var(--ink);
  }
  .wine-label__artwork {
    position: absolute;
    left: 70px;
    top: 140px;
    width: 412px;
    height: 320px;
  }
  .wine-label__grape {
    position: absolute;
    top: 468px;
    left: 0;
    width: 100%;
    text-align: center;
    font-family: "Archivo Black", "Arial Black", sans-serif;
    font-size: 52px;
    letter-spacing: 1px;
    line-height: 1;
    color: var(--ink);
  }
  .wine-label__style,
  .wine-label__vintage {
    position: absolute;
    left: 0;
    width: 100%;
    text-align: center;
    font-family: "Arimo", Arial, sans-serif;
    font-size: 22px;
    line-height: 1;
    color: var(--ink-dark);
  }
  .wine-label__style { top: 550px; }
  .wine-label__vintage { top: 590px; }
</style>
</head>
<body>
  <main class="stage">
    <section class="wine-label">
      <div class="wine-label__paper">
        <h1 class="wine-label__name">Kieselwind</h1>
        <svg class="wine-label__artwork" viewBox="0 0 412 320" role="img" aria-label="Watercolour splash in red, violet and blue with two white bare footprints">
          <defs>
            <radialGradient id="splash-red">
              <stop offset="0" stop-color="var(--splash-red)" stop-opacity="0.85"/>
              <stop offset="0.6" stop-color="var(--splash-red)" stop-opacity="0.4"/>
              <stop offset="1" stop-color="var(--splash-red)" stop-opacity="0"/>
            </radialGradient>
            <radialGradient id="splash-blue">
              <stop offset="0" stop-color="var(--splash-blue)" stop-opacity="0.85"/>
              <stop offset="0.6" stop-color="var(--splash-blue)" stop-opacity="0.4"/>
              <stop offset="1" stop-color="var(--splash-blue)" stop-opacity="0"/>
            </radialGradient>
            <radialGradient id="splash-violet">
              <stop offset="0" stop-color="var(--splash-violet)" stop-opacity="0.6"/>
              <stop offset="1" stop-color="var(--splash-violet)" stop-opacity="0"/>
            </radialGradient>
          </defs>
          <ellipse cx="140" cy="210" rx="120" ry="95" fill="url(#splash-red)"/>
          <ellipse cx="270" cy="120" rx="135" ry="105" fill="url(#splash-blue)"/>
          <ellipse cx="205" cy="165" rx="110" ry="90" fill="url(#splash-violet)"/>
        </svg>
        <p class="wine-label__grape">RIESLING</p>
        <p class="wine-label__style">TROCKEN</p>
        <p class="wine-label__vintage">2014</p>
      </div>
    </section>
  </main>
</body>
</html>
```